Cleaning Company Website Design

I am looking for a website design that has my contact information on each page (Call or Text and my e-mail). It should have the main landing page and than pages for Residential Cleaning (Move In/Move Out, Weekly, and Bi-Weekly Cleaning), Commercial Cleaning (Move In/Move Out, Weekly, and Bi-Weekly Cleaning), New Construction Cleaning (Residential, Commercial, and Industrial), and Apartment Turn cleaning for Property Managers. It should list that we carry insurance as well.

Target Market(s)

Residential and Commercial Customers

Industry/Entity Type

Cleaning

Coding

Coded - Design and coding required

Number of Pages Required

5+ page

Requirements
Must have
• A clean professional looking website

```html
<!DOCTYPE html>
<html lang="en">
<head>
<meta charset="utf-8">
<title>BrightNest Cleaning – Residential Cleaning</title>
<link href="https://fonts.googleapis.com/css2?family=Lexend+Exa:wght@600&family=Roboto:wght@400;500;700&display=swap" rel="stylesheet">
<style>
:root{
  --teal:#2bb3a5;
  --blue:#146a99;
  --navy:#125d89;
  --yellow:#f0c21b;
  --yellow-soft:#f8e6a0;
  --teal-soft:#bfe9e3;
  --ink:#1d1d1d;
  --text:#4a4a4a;
  --line:#e6e6e6;
  --white:#ffffff;
}
*{box-sizing:border-box;margin:0;padding:0}
html,body{width:1200px;height:3633px;overflow:hidden}
body{position:relative;background:var(--white);font-family:"Roboto",sans-serif;color:var(--text)}
.abs{position:absolute}
.display{font-family:"Lexend Exa",sans-serif;font-weight:600;letter-spacing:0;line-height:1.15}
.teal{color:var(--teal)}
.blue{color:var(--blue)}

/* header */
.site-header{position:absolute;left:0;top:0;width:1200px;height:151px;background:var(--white);z-index:3}
.brand{position:absolute;left:111px;top:54px;color:var(--teal);font-family:"Roboto",sans-serif;font-weight:500;text-align:center;line-height:1}
.brand .name{font-size:30px;letter-spacing:2px;display:block}
.brand .sub{font-size:14px;letter-spacing:4px;display:block;margin-top:4px}
.contact-chip{position:absolute;top:25px;display:flex;align-items:center;gap:16px}
.chip-icon{width:52px;height:52px;border-radius:50%;background:var(--yellow);display:flex;align-items:center;justify-content:center}
.chip-label{font-size:11px;font-weight:700;color:var(--ink);letter-spacing:.3px}
.chip-value{font-size:15px;font-weight:500;color:var(--blue);margin-top:6px}
.main-nav{position:absolute;top:106px;left:519px;display:flex;gap:0;font-size:14px;font-weight:500;color:var(--ink)}
.main-nav a{position:absolute;white-space:nowrap;color:inherit;text-decoration:none}
.main-nav .active{color:var(--teal)}
.main-nav .active::after{content:"";position:absolute;left:0;right:22px;bottom:-8px;height:2px;background:var(--yellow)}
.social{position:absolute;width:36px;height:36px;border-radius:50%}
.social.fill{background:var(--blue)}
.social.outline{background:var(--white);box-shadow:0 2px 8px rgba(0,0,0,.15)}
.social::after{content:"";position:absolute;left:13px;top:13px;width:10px;height:10px;border-radius:50%}
.social.fill::after{background:var(--white)}
.social.outline::after{border:2px solid var(--blue)}

/* hero */
.hero-photo{position:absolute;left:0;top:151px;width:1200px;height:560px;
  background:linear-gradient(90deg,#dfeaf0 0%,#b9d0dc 30%,#8fb7cd 48%,#2a7fc1 62%,#e7c53b 80%,#6d7a86 100%)}
.hero-waves{position:absolute;left:0;top:520px;z-index:1}
.hero-title{position:absolute;left:111px;top:346px;font-size:45px;z-index:2}
.scroll-btn{position:absolute;left:570px;top:614px;width:60px;height:60px;border-radius:50%;background:var(--white);box-shadow:0 4px 14px rgba(0,0,0,.15);display:flex;align-items:center;justify-content:center;z-index:2}

/* content */
.intro{position:absolute;left:111px;top:766px;width:974px;font-size:15.5px;line-height:27.5px;z-index:2}
.intro p+p{margin-top:18px}
.service-title{position:absolute;font-size:37px;white-space:nowrap}
.rule{position:absolute;height:3px;width:94px;background:var(--yellow)}
.service-text{position:absolute;width:489px;font-size:15.5px;line-height:27.5px;text-align:justify}
.service-text p+p{margin-top:14px}
.ring{position:absolute;width:430px;height:430px;border-radius:50%}
.ring .photo{position:absolute;width:412px;height:412px;border-radius:50%}

/* contact */
.contact-title{position:absolute;left:0;width:1200px;top:2618px;text-align:center;font-size:45px}
.contact-form{position:absolute;left:601px;top:2726px;width:510px}
.field{position:absolute}
.field label{display:block;font-size:15px;font-weight:500;color:var(--ink);margin-bottom:8px}
.field .box{height:38px;background:var(--white);box-shadow:0 2px 10px rgba(0,0,0,.12);font-size:13px;color:#8a8a8a;padding:11px 19px;position:relative}
.submit{position:absolute;left:1px;top:386px;width:141px;height:48px;border-radius:24px;background:var(--yellow);font-size:15px;font-weight:700;color:var(--ink);display:flex;align-items:center;justify-content:center}

/* footer */
.site-footer{position:absolute;left:0;top:3340px;width:1200px;height:293px;background:var(--navy)}
.foot-brand{position:absolute;left:111px;top:3466px;color:var(--white);font-weight:500;text-align:center;line-height:1}
.foot-brand .name{font-size:34px;letter-spacing:2px;display:block}
.foot-brand .sub{font-size:17px;letter-spacing:4px;display:block;margin-top:6px}
.foot-col{position:absolute;color:var(--white)}
.foot-col h4{font-size:17px;font-weight:500;margin-bottom:22px}
.foot-col ul{list-style:none}
.foot-col li{font-size:14px;display:flex;align-items:center;gap:22px;height:39.5px}
.dot{width:13px;height:13px;border-radius:50%;background:var(--yellow);position:relative;flex:none}
.dot::after{content:"";position:absolute;left:3px;top:4px;border-left:6px solid var(--navy);border-top:2.5px solid transparent;border-bottom:2.5px solid transparent}
.info-row{display:flex;gap:20px;margin-bottom:18px}
.info-row b{display:block;font-size:14px;font-weight:500}
.info-row span{display:block;font-size:12px;margin-top:5px}
.touch-text{font-size:14px;font-weight:700;line-height:27.5px;width:287px;text-align:justify}
.touch-btn{margin-top:16px;width:126px;height:38px;border-radius:19px;background:var(--yellow);color:var(--ink);font-size:11px;font-weight:700;display:flex;align-items:center;justify-content:center}
.foot-rule{position:absolute;left:111px;top:3563px;width:978px;height:1px;background:rgba(255,255,255,.3)}
.copyright{position:absolute;left:0;width:1200px;top:3587px;text-align:center;color:var(--white);font-size:12.5px}
.copyright b{font-weight:500}
</style>
</head>
<body>

<header class="site-header">
  <div class="brand"><span class="name">BRIGHTNEST</span><span class="sub">CLEANING</span></div>

  <div class="contact-chip" style="left:606px">
    <div class="chip-icon">
      <svg width="22" height="22" viewBox="0 0 24 24"><path fill="#1d1d1d" d="M6.6 10.8a15.1 15.1 0 0 0 6.6 6.6l2.2-2.2c.3-.3.7-.4 1-.2 1.1.4 2.3.6 3.6.6.6 0 1 .4 1 1V20c0 .6-.4 1-1 1A17 17 0 0 1 3 4c0-.6.4-1 1-1h3.5c.6 0 1 .4 1 1 0 1.3.2 2.5.6 3.6.1.3 0 .7-.2 1z"/></svg>
    </div>
    <div><div class="chip-label">CALL OR TEXT:</div><div class="chip-value">(555) 014 - 2738</div></div>
  </div>

  <div class="contact-chip" style="left:819px">
    <div class="chip-icon">
      <svg width="22" height="22" viewBox="0 0 24 24"><path fill="#1d1d1d" d="M3 9l9-6 9 6v11H3z"/><path fill="#f0c21b" d="M5 10.5l7 4.5 7-4.5V19H5z"/><path fill="none" stroke="#1d1d1d" stroke-width="1.3" d="M5 19l5.5-5M19 19l-5.5-5"/></svg>
    </div>
    <div><div class="chip-label">EMAIL US:</div><div class="chip-value">hello@brightnestclean.com</div></div>
  </div>

  <nav class="main-nav">
    <a style="left:0">HOME</a>
    <a style="left:84px">ABOUT US</a>
    <a class="active" style="left:197px">OUR SERVICES&nbsp;&nbsp;<svg width="10" height="8" viewBox="0 0 10 8"><path d="M1 2l4 4 4-4" fill="none" stroke="#1d1d1d" stroke-width="1.6"/></svg></a>
    <a style="left:361px">CONTACT US</a>
  </nav>
  <span class="social fill" style="left:1007px;top:96px" aria-label="Social profile"></span>
  <span class="social outline" style="left:1052px;top:96px" aria-label="Social profile"></span>
</header>

<div class="hero-photo" role="img" aria-label="Blue bucket filled with spray bottles, sponges and cleaning supplies carried by a gloved hand"></div>
<svg class="hero-waves" width="1200" height="240" viewBox="0 0 1200 240">
  <path fill="#ffffff" d="M0 215 C150 110 300 88 450 100 C650 120 800 175 950 165 C1080 155 1150 90 1200 20 L1200 240 L0 240 Z"/>
  <path fill="var(--yellow-soft)" d="M0 240 L0 195 C110 125 240 95 360 93 C240 115 110 165 30 240 Z"/>
  <path fill="var(--yellow)" d="M0 235 L0 205 C110 135 230 103 330 96 C220 120 100 170 0 235 Z"/>
  <path fill="var(--teal-soft)" d="M1200 55 C1140 140 1060 170 940 168 C1070 180 1160 140 1200 110 Z"/>
  <path fill="var(--teal)" d="M1200 25 C1140 120 1060 160 950 166 C1080 165 1160 115 1200 75 Z"/>
</svg>
<h1 class="display hero-title"><span class="teal">RESIDENTIAL</span><br><span class="blue">CLEANING</span></h1>
<div class="scroll-btn"><svg width="18" height="18" viewBox="0 0 18 18"><path d="M3 3l6 5 6-5M3 9l6 5 6-5" fill="none" stroke="var(--teal)" stroke-width="2.2"/></svg></div>

<section class="intro">
  <p>Lorem ipsum dolor sit amet, consectetur adipiscing elit, sed do eiusmod tempor incididunt ut labore et dolore magna aliqua. Ut enim ad minim veniam, quis nostrud exercitation ullamco laboris nisi ut aliquip ex ea commodo consequat. Duis aute irure dolor in reprehenderit in voluptate velit esse cillum dolore eu fugiat nulla pariatur. Excepteur sint occaecat cupidatat non proident, sunt in culpa qui officia deserunt mollit anim id est laborum perspiciatis unde omnis iste natus error sit voluptatem accusantium doloremque laudantium.</p>
  <p>Lorem ipsum dolor sit amet, consectetur adipiscing elit, sed do eiusmod tempor incididunt ut labore et dolore magna aliqua. Ut enim ad minim veniam, quis nostrud exercitation ullamco laboris nisi ut aliquip ex ea commodo consequat. Duis aute irure dolor in reprehenderit in voluptate velit esse cillum dolore eu fugiat nulla pariatur.</p>
</section>

<!-- Move in / move out -->
<h2 class="display service-title" style="left:111px;top:1078px"><span class="teal">MOVE IN/</span><span class="blue">MOVE OUT</span></h2>
<div class="rule" style="left:111px;top:1125px"></div>
<div class="service-text" style="left:111px;top:1159px">
  <p>Lorem ipsum dolor sit amet, consectetur adipiscing elit, sed do eiusmod tempor incididunt ut labore et dolore magna aliqua. Ut enim ad minim veniam, quis nostrud exercitation ullamco laboris nisi ut aliquip ex ea commodo consequat. Duis aute irure dolor in reprehenderit in voluptate velit esse cillum dolore eu fugiat nulla pariatur. Excepteur sint occaecat cupidatat non proident, sunt in culp.</p>
  <p>Lorem ipsum dolor sit amet, consectetur adipiscing elit, sed do eiusmod tempor incididunt ut labore et dolore magna aliqua. Ut enim ad minim veniam, quis nostrud exercitation ullamco laboris nisi ut aliquip ex ea commodo consequat.</p>
</div>
<div class="ring" style="left:659px;top:1049px;background:var(--blue)">
  <div class="photo" style="left:0;top:9px;background:radial-gradient(circle at 55% 40%,#f1e7da 0%,#c9a27a 55%,#8a5a36 100%)" role="img" aria-label="Bright room with stacked moving boxes and potted plants"></div>
</div>

<!-- Weekly -->
<div class="ring" style="left:111px;top:1559px;background:var(--yellow)">
  <div class="photo" style="left:9px;top:18px;background:radial-gradient(circle at 45% 45%,#eef0ee 0%,#d8d6cf 55%,#c9b34a 100%)" role="img" aria-label="Gloved hands spraying and wiping a white surface"></div>
</div>
<h2 class="display service-title" style="left:601px;top:1588px"><span class="teal">WEEKLY</span> <span class="blue">CLEANING</span></h2>
<div class="rule" style="left:601px;top:1635px"></div>
<div class="service-text" style="left:601px;top:1669px">
  <p>Lorem ipsum dolor sit amet, consectetur adipiscing elit, sed do eiusmod tempor incididunt ut labore et dolore magna aliqua. Ut enim ad minim veniam, quis nostrud exercitation ullamco laboris nisi ut aliquip ex ea commodo consequat. Duis aute irure dolor in reprehenderit in voluptate velit esse cillum dolore eu fugiat nulla pariatur. Excepteur sint occaecat cupidatat non proident, sunt in culp.</p>
  <p>Lorem ipsum dolor sit amet, consectetur adipiscing elit, sed do eiusmod tempor incididunt ut labore et dolore magna aliqua. Ut enim ad minim veniam, quis nostrud exercitation ullamco laboris nisi ut aliquip ex ea commodo consequat.</p>
</div>

<!-- Bi-weekly -->
<h2 class="display service-title" style="left:111px;top:2098px"><span class="teal">BI-WEEKLY</span> <span class="blue">CLEANING</span></h2>
<div class="rule" style="left:111px;top:2145px"></div>
<div class="service-text" style="left:111px;top:2179px">
  <p>Lorem ipsum dolor sit amet, consectetur adipiscing elit, sed do eiusmod tempor incididunt ut labore et dolore magna aliqua. Ut enim ad minim veniam, quis nostrud exercitation ullamco laboris nisi ut aliquip ex ea commodo consequat. Duis aute irure dolor in reprehenderit in voluptate velit esse cillum dolore eu fugiat nulla pariatur. Excepteur sint occaecat cupidatat non proident, sunt in culp.</p>
  <p>Lorem ipsum dolor sit amet, consectetur adipiscing elit, sed do eiusmod tempor incididunt ut labore et dolore magna aliqua. Ut enim ad minim veniam, quis nostrud exercitation ullamco laboris nisi ut aliquip ex ea commodo consequat.</p>
</div>
<div class="ring" style="left:659px;top:2069px;background:var(--teal)">
  <div class="photo" style="left:0;top:9px;background:radial-gradient(circle at 60% 45%,#f2f4f2 0%,#9fd0dc 45%,#2a9fcf 75%,#8a9a6a 100%)" role="img" aria-label="Blue-gloved hands spraying and wiping a kitchen counter"></div>
</div>

<!-- Contact -->
<h2 class="display contact-title"><span class="teal">CONTACT</span> <span class="blue">US</span></h2>
<div class="rule" style="left:553px;top:2674px"></div>
<div class="ring" style="left:111px;top:2731px;background:var(--yellow)">
  <div class="photo" style="left:9px;top:18px;background:radial-gradient(circle at 55% 50%,#e9edf0 0%,#9cc3d8 45%,#7a8896 80%,#c25aa0 100%)" role="img" aria-label="Blue bucket with yellow rubber gloves, mop and cleaning bottles on a tiled floor"></div>
</div>

<form class="contact-form">
  <div class="field" style="left:0;top:0;width:250px"><label>Name</label><div class="box">Your Name</div></div>
  <div class="field" style="left:259px;top:0;width:250px"><label>City/Town</label><div class="box">Your City/Town</div></div>
  <div class="field" style="left:0;top:84px;width:250px"><label>Email</label><div class="box">Your Email</div></div>
  <div class="field" style="left:259px;top:84px;width:250px"><label>Phone</label><div class="box">Your Phone</div></div>
  <div class="field" style="left:0;top:167px;width:509px"><label>Services</label><div class="box">Select<svg style="position:absolute;right:16px;top:15px" width="10" height="8" viewBox="0 0 10 8"><path d="M1 2l4 4 4-4" fill="none" stroke="#1d1d1d" stroke-width="1.6"/></svg></div></div>
  <div class="field" style="left:0;top:250px;width:509px"><label>Comment</label><div class="box" style="height:91px">Enter Your Comment</div></div>
  <div class="submit">SUBMIT</div>
</form>

<!-- Footer -->
<svg class="abs" style="left:0;top:3150px" width="1200" height="200" viewBox="0 0 1200 200">
  <path fill="var(--navy)" d="M0 200 L0 145 C150 85 300 65 450 85 C650 115 850 150 1000 122 C1100 102 1160 62 1200 30 L1200 200 Z"/>
  <path fill="var(--teal-soft)" d="M0 195 L0 150 C100 88 210 66 320 70 C200 88 90 135 0 195 Z"/>
  <path fill="var(--teal)" d="M0 200 L0 170 C100 100 210 76 300 72 C200 95 90 145 0 200 Z"/>
  <path fill="var(--yellow-soft)" d="M1200 0 C1150 70 1060 120 930 140 C1060 135 1150 80 1200 30 Z"/>
  <path fill="var(--yellow)" d="M1200 40 C1150 100 1060 135 930 142 C1070 150 1160 110 1200 80 Z"/>
</svg>
<footer class="site-footer"></footer>
<div class="foot-brand"><span class="name">BRIGHTNEST</span><span class="sub">CLEANING</span></div>

<div class="foot-col" style="left:376px;top:3362px">
  <h4>QUICK LINKS</h4>
  <ul>
    <li><span class="dot"></span>Home</li>
    <li><span class="dot"></span>About Us</li>
    <li><span class="dot"></span>Our Services</li>
    <li><span class="dot"></span>Contact Us</li>
  </ul>
</div>

<div class="foot-col" style="left:551px;top:3362px">
  <h4>CONTACT INFO</h4>
  <div class="info-row">
    <svg width="14" height="14" viewBox="0 0 24 24"><path fill="var(--yellow)" d="M6.6 10.8a15.1 15.1 0 0 0 6.6 6.6l2.2-2.2c.3-.3.7-.4 1-.2 1.1.4 2.3.6 3.6.6.6 0 1 .4 1 1V20c0 .6-.4 1-1 1A17 17 0 0 1 3 4c0-.6.4-1 1-1h3.5c.6 0 1 .4 1 1 0 1.3.2 2.5.6 3.6.1.3 0 .7-.2 1z"/></svg>
    <div><b>PHONE:</b><span>(555) 014 - 2738</span></div>
  </div>
  <div class="info-row">
    <svg width="14" height="14" viewBox="0 0 24 24"><path fill="var(--yellow)" d="M2 5h20v14H2z"/><path fill="none" stroke="var(--navy)" stroke-width="2" d="M2 6l10 7 10-7"/></svg>
    <div><b>EMAIL:</b><span>hello@brightnestclean.com</span></div>
  </div>
</div>

<div class="foot-col" style="left:801px;top:3362px">
  <h4>GET IN TOUCH</h4>
  <p class="touch-text">Lorem ipsum dolor sit amet, consectetur adipiscing elit, sed do eiusmod tempor incididunt ut laborea.</p>
  <div class="touch-btn">CONTACT US</div>
</div>

<div class="foot-rule"></div>
<p class="copyright">© 2024 <b>BRIGHTNEST CLEANING</b> &nbsp;|&nbsp; All Rights Reserved</p>
<span class="social" style="left:1007px;top:3576px;background:var(--yellow)" aria-label="Social profile"></span>
<span class="social" style="left:1052px;top:3576px;background:var(--white)" aria-label="Social profile"></span>

</body>
</html>
```